Real Estate "For Sale" Sign for construction company

We need a sign that we can use to hang on a post and place on the road when we sell a property. The sign will be simple and will need to mainly feature our logo (files attached), as well as the words "For Sale", and then our phone number "(555) 617 3489". The sign will hang on a post that'll look something like the attached picture.

Target Market(s)

Home buyers

Industry/Entity Type

Real Estate

Font styles to use
Serif
Sans Serif

Colors
0054AA
0677BA
7BADD7
CADEEF
E8F1F8
0094D4
00A9DD
6FCCEA
C7EBF8
E9F6FB

Requirements
Must have
• For Sale & our phone number

```html
<!DOCTYPE html>
<html lang="en">
<head>
<meta charset="utf-8">
<title>Cedar Ridge Properties – For Sale Sign</title>
<link href="https://fonts.googleapis.com/css2?family=Roboto+Condensed:wght@700&display=swap" rel="stylesheet">
<style>
  :root {
    --backdrop: #6d6e71;
    --sky: #8dd6f5;
    --navy: #141f4d;
    --accent-band: #0a4fa3;
    --white: #ffffff;
  }
  html, body {
    margin: 0;
    padding: 0;
    width: 1200px;
    height: 879px;
    overflow: hidden;
    background: var(--backdrop);
  }
  .canvas {
    position: relative;
    width: 1200px;
    height: 879px;
  }
  .sale-sign {
    position: absolute;
    left: 220px;
    top: 60px;
    width: 760px;
    height: 760px;
    display: block;
  }
  .sign-sky { fill: var(--sky); }
  .sign-band { fill: var(--accent-band); }
  .sign-base { fill: var(--navy); }
  .brand-name {
    font-family: "Roboto Condensed", sans-serif;
    font-weight: 700;
    font-size: 58px;
    fill: var(--navy);
  }
  .sale-heading {
    font-family: "Roboto Condensed", sans-serif;
    font-weight: 700;
    font-size: 165px;
    fill: var(--white);
  }
  .sale-phone {
    font-family: "Roboto Condensed", sans-serif;
    font-weight: 700;
    font-size: 108px;
    fill: var(--white);
  }
</style>
</head>
<body>
<main class="canvas">
  <svg class="sale-sign" viewBox="0 0 760 760" xmlns="http://www.w3.org/2000/svg">
    <rect class="sign-sky" x="0" y="0" width="760" height="760"/>
    <path class="sign-band" d="M0,417 Q380,171 760,417 L760,760 L0,760 Z"/>
    <path class="sign-base" d="M0,447 Q380,181 760,447 L760,760 L0,760 Z"/>
    <text class="brand-name" x="380" y="230" text-anchor="middle">Cedar Ridge Properties</text>
    <text class="sale-heading" x="380" y="545" text-anchor="middle">FOR SALE</text>
    <text class="sale-phone" x="380" y="695" text-anchor="middle">(555) 617 3489</text>
  </svg>
</main>
</body>
</html>
```